Business Card Ayurvedic Massage

I'm starting with my ayurvedic massage business and need a business card design. The design should be inline with my brand/logo as well as with the design of my website (www.lumo-thara.ch).
Front: logo and text "Ayurvedische Massagen"
back: name and adress (see details https://www.lumo-thara.ch/kontakt.html)

```html
<!DOCTYPE html>
<html lang="de">
<head>
<meta charset="utf-8">
<title>lumo-thara – Visitenkarte</title>
<link rel="stylesheet" href="https://fonts.googleapis.com/css2?family=Cinzel:wght@700&family=Open+Sans:wght@500&display=swap">
<style>
  :root {
    --maroon: #8a1a12;
    --maroon-deep: #6e120c;
    --maroon-soft: #9a2a20;
    --gold: #e0a63a;
    --gold-strip-top: #d9a412;
    --orange-strip-bottom: #fb8a4e;
    --blush: #f7bfa5;
    --ink: #111111;
    --paper: #ffffff;
    --leaf-green: #5fc12a;
  }
  html, body {
    margin: 0;
    padding: 0;
    overflow: hidden;
    background: var(--paper);
  }
  .card {
    position: relative;
    width: 1200px;
    height: 720px;
    overflow: hidden;
    background: var(--paper);
  }
  .brand-panel {
    position: absolute;
    left: 0; top: 0;
    width: 482px; height: 720px;
    background: radial-gradient(ellipse at 50% 40%, var(--maroon-soft), var(--maroon) 60%, var(--maroon-deep));
  }
  .accent-strip {
    position: absolute;
    left: 482px; top: 0;
    width: 36px; height: 720px;
    background: linear-gradient(180deg, var(--gold-strip-top), var(--orange-strip-bottom));
  }
  .brand-name {
    position: absolute;
    left: 0; top: 248px;
    width: 530px;
    text-align: center;
    font-family: "Cinzel", serif;
    font-weight: 700;
    font-size: 32px;
    color: var(--gold);
    letter-spacing: 1px;
  }
  .brand-tagline {
    position: absolute;
    left: 0; top: 330px;
    width: 544px;
    text-align: center;
    font-family: "Open Sans", sans-serif;
    font-weight: 500;
    font-size: 19px;
    color: var(--blush);
    letter-spacing: 0.5px;
  }
  .monument {
    position: absolute;
    left: 94px; top: 416px;
    width: 370px; height: 216px;
    background: linear-gradient(180deg, rgba(190,80,70,0.25), rgba(190,80,70,0.4));
    border-radius: 120px 120px 0 0;
  }
  .side-tab {
    position: absolute;
    right: 0; top: 0;
    width: 70px; height: 720px;
  }
  .contact-icon {
    position: absolute;
    width: 88px; height: 88px;
  }
  .contact-text {
    position: absolute;
    left: 697px;
    margin: 0;
    font-family: "Cinzel", serif;
    font-weight: 700;
    color: var(--ink);
    white-space: nowrap;
  }
  .contact-phone { top: 186px; font-size: 36px; letter-spacing: 1px; }
  .contact-mail { top: 302px; font-size: 26px; letter-spacing: 1px; }
  .contact-address { top: 398px; max-width: 420px; font-size: 23px; line-height: 31px; letter-spacing: 0.3px; }
  .herb-badge {
    position: absolute;
    left: 1013px; top: 535px;
    width: 152px; height: 146px;
    border-radius: 50%;
    background: radial-gradient(circle at 45% 40%, #a6e34a, var(--leaf-green) 55%, #2e8a16);
  }
</style>
</head>
<body>
<div class="card">
  <section class="brand-panel">
    <div class="brand-name">lumo-thara</div>
    <div class="brand-tagline">AYURVEDISCHE MASSAGEN</div>
    <div class="monument" role="img" aria-label="Faint illustration of a domed Indian palace with minarets"></div>
  </section>
  <div class="accent-strip"></div>

  <svg class="side-tab" viewBox="0 0 70 720" aria-hidden="true">
    <polygon points="0,160 70,124 70,530 0,497" fill="#8a1a12"/>
    <polygon points="0,160 70,124 70,140 0,172" fill="#6e120c"/>
  </svg>

  <div class="contact-list">
    <svg class="contact-icon" style="left:562px;top:164px" viewBox="0 0 88 88" aria-hidden="true">
      <defs>
        <linearGradient id="ringGrad" x1="0" y1="0" x2="0" y2="1">
          <stop offset="0" stop-color="#f8c219"/>
          <stop offset="1" stop-color="#ee5a1c"/>
        </linearGradient>
      </defs>
      <circle cx="44" cy="44" r="43" fill="url(#ringGrad)"/>
      <circle cx="44" cy="44" r="37" fill="none" stroke="#ee5a1c" stroke-width="4" stroke-dasharray="4 4"/>
      <circle cx="44" cy="44" r="32" fill="#111"/>
      <path d="M33 28c2-2 5-2 6 0l3 6c1 2 0 4-1 5l-2 2c2 4 5 7 9 9l2-2c1-1 3-2 5-1l6 3c2 1 2 4 0 6l-3 3c-3 2-8 2-14-2-6-4-11-9-14-15-3-6-3-11 0-14z" fill="#fff"/>
    </svg>
    <p class="contact-text contact-phone">+41 77 555 28 14</p>

    <svg class="contact-icon" style="left:562px;top:283px" viewBox="0 0 88 88" aria-hidden="true">
      <circle cx="44" cy="44" r="43" fill="url(#ringGrad)"/>
      <circle cx="44" cy="44" r="37" fill="none" stroke="#ee5a1c" stroke-width="4" stroke-dasharray="4 4"/>
      <circle cx="44" cy="44" r="32" fill="#111"/>
      <text x="44" y="55" text-anchor="middle" font-family="Open Sans, sans-serif" font-size="34" font-weight="500" fill="#fff">@</text>
    </svg>
    <p class="contact-text contact-mail">INFO@LUMO-THARA.CH</p>

    <svg class="contact-icon" style="left:570px;top:404px" viewBox="0 0 88 88" aria-hidden="true">
      <circle cx="44" cy="44" r="43" fill="url(#ringGrad)"/>
      <circle cx="44" cy="44" r="37" fill="none" stroke="#ee5a1c" stroke-width="4" stroke-dasharray="4 4"/>
      <circle cx="44" cy="44" r="32" fill="#111"/>
      <rect x="26" y="32" width="36" height="25" rx="3" fill="#fff"/>
      <polyline points="27,34 44,47 61,34" fill="none" stroke="#111" stroke-width="2"/>
    </svg>
    <p class="contact-text contact-address">LINA BERGER, LUMO-THARA,<br>LINDENWEG 14,<br>8857 TALMATT (SZ)</p>
  </div>

  <div class="herb-badge" role="img" aria-label="Illustration of green leaves above a herbal mortar and pestle"></div>
</div>
</body>
</html>
```